Professional, Elegant, Modern and Playful business card Design for an Orthodontist (Dentist)

We need a new business card design for an Orthodontist (Dentist).
We would like to see designs that are elegant, but also playful. The designs and colors should be in harmony with the existing logo (uploaded).
Size: standard size (85mm x 55mm)
The font of the logo text is roboto (Google), you don't need to use the same font, but the used font has to be in harmony with the font used in the logo.
The colors used have to be in harmony with the logo.

Target Market(s)

Orthodontist (Dentist)

Industry/Entity Type

Dental Clinic

Contact Information for Business Card

* Size: standard size (85mm x 55mm)
* The font of the logo text is roboto (Google), you don't need to use the same font, but the used font has to be in harmony with the font used in the logo.
* The colors used have to be in harmony with the logo.

* Following Information have to be on the front side:
- Logo with company name (see uploaded files) as a unit
or
- separate the logo from the text and position them separately
- Text that has to be on the front side:
Kieferorthopädie Brunnweid
Dr. med. dent. Lukas Venberg
Fachzahnarzt für Kieferorthopädie (CH)
(if there is enough space, please also write:
Eidg. dipl. Zahnarzt, Mitglied VZB und FOV)
(address:)
Talackerweg 7
8946 Schlieren
(telephone number:)
044 618 42 50
(if there is much space left, also fax number, but it is not mandatory:
044 618 42 51)
info@brunnweidpraxis.net
www.brunnweidpraxis.net
(If there is space left:
QR-code with the homepage-adress: www.brunnweidpraxis.net
and in the center of the QR-Code a little logo)
- It is important not to overload the front side. Put in the optional parts on the front side only if it doesn't look overloaded.

* Following Information have to be on the back side:
- An abstract map sketch (freehand drawing) of the location of the office is uploaded (Map on the back side of the business card.pdf). Please do a nicely designed abstract map based on this sketch.
- Feel free to change everything to make it good.
- For better reading the text has been rewritten in the sketch on the outside of the border of the card.
- You can see the original situation e.g. in google maps (Address: Talackerweg 7, 8946 Schlieren, Switzerland)
- Marked as yellow are the important streets. These should not be yellow in the final design.
- The symbols of the freeway (green symbol) and the car park are uploaded ad vector graphics.
- "A1" should be the same green color as the background of the freeway (green symbol).
- The symbols of the bus stops and the railway station are uploaded as pixel graphics. Please convert them to vector graphics and make the background blue the same.
- The badges of the train numbers (S3 and S12) and bus numbers (31, 302, 303, 307, 308) are also pixel graphics. Please draw them as vector graphics. The font doesn't have to be identical with the one in the sketch, but the color codes need to be the same in the final design.
- The dashed blue line is a footway only. It should not be drawn like this in the final design. The design decision is up to you, but it should be different from the streets.
- The building of the office and the arrow showing the entrance should be clearly
visible and distinguishable form the other drawings.

Font styles to use
Sans Serif

Colors

Designer to choose colors to be used in the design.

Requirements
Must have
• - vector graphics
• - vector files: adobe illustrator or compatible
Should not have
• - pixel graphics

```html
<!DOCTYPE html>
<html lang="de">
<head>
<meta charset="utf-8">
<title>Kieferorthopädie Brunnweid – Visitenkarte</title>
<link rel="stylesheet" href="https://fonts.googleapis.com/css2?family=Roboto:wght@400;500;700&display=swap">
<style>
  :root {
    --navy: #232262;
    --sky: #29abe2;
    --white: #ffffff;
    --grey-text: #6b6b78;
    --map-grey: #d3d4d8;
    --map-road: #c4b8ad;
    --bg-red: #d8242f;
    --bg-purple: #9b3a9a;
    --bg-violet: #4b3a9a;
  }
  * { margin: 0; padding: 0; box-sizing: border-box; }
  html, body { width: 1200px; height: 1000px; overflow: hidden; }
  body {
    position: relative;
    font-family: "Roboto", Arial, sans-serif;
    background: linear-gradient(135deg, var(--bg-red) 0%, var(--bg-purple) 50%, var(--bg-violet) 100%);
  }
  .card { position: absolute; overflow: hidden; background: var(--navy); }
  .card-back { left: 35px; top: 87px; width: 540px; height: 806px; }
  .card-front { left: 632px; top: 87px; width: 545px; height: 810px; }
  .card-svg { position: absolute; inset: 0; }
  .map-frame {
    position: absolute; left: 57px; top: 65px; width: 426px; height: 676px;
    background: var(--white); padding: 7px;
  }
  .map-area {
    width: 100%; height: 100%;
    background: linear-gradient(160deg, var(--map-grey) 0%, #cdc6c0 55%, var(--map-road) 100%);
  }
  .logo-spot {
    position: absolute; left: 230px; top: 62px; width: 86px; height: 86px;
    border-radius: 50%; background: var(--navy);
  }
  .practice-name {
    position: absolute; left: 98px; top: 182px;
    font-size: 26px; font-weight: 700; color: var(--navy); letter-spacing: -0.2px;
  }
  .doctor-name {
    position: absolute; left: 98px; top: 219px;
    font-size: 20px; font-weight: 400; color: var(--grey-text); letter-spacing: 0.3px;
  }
  .doctor-title {
    position: absolute; left: 98px; top: 244px;
    font-size: 17px; font-weight: 400; color: var(--grey-text); letter-spacing: 0.3px;
  }
  .contact-list { position: absolute; left: 61px; top: 448px; list-style: none; }
  .contact-item {
    position: relative; display: flex; align-items: center;
    height: 40px; margin-bottom: 46px; padding: 0 10px 0 52px;
    background: var(--white); border-radius: 20px;
    font-size: 22px; color: var(--navy); letter-spacing: 0.3px; white-space: nowrap;
  }
  .contact-icon {
    position: absolute; left: 1px; top: 1px; width: 38px; height: 38px;
    border-radius: 50%; background: var(--sky);
    display: flex; align-items: center; justify-content: center;
    box-shadow: inset 0 0 0 3px #bfe6f7;
  }
  .contact-icon svg { width: 20px; height: 20px; }
</style>
</head>
<body>

<section class="card card-back" aria-label="Rückseite mit Lageplan">
  <svg class="card-svg" width="540" height="806" viewBox="0 0 540 806">
    <path d="M0,228 C150,262 330,320 540,368 L540,412 C330,372 140,330 0,312 Z" fill="var(--sky)"/>
  </svg>
  <div class="map-frame">
    <div class="map-area" role="img" aria-label="Abstrakter Lageplan der Praxis am Talackerweg 7 in Schlieren mit Bahnhof, Bushaltestellen, Autobahn A1 und Parkhaus"></div>
  </div>
</section>

<section class="card card-front" aria-label="Vorderseite">
  <svg class="card-svg" width="545" height="810" viewBox="0 0 545 810">
    <path d="M0,245 C140,300 330,415 545,385 L545,810 L0,810 Z" fill="var(--sky)"/>
    <path d="M0,0 H545 V338 C330,370 140,270 0,195 Z" fill="var(--white)"/>
    <path d="M0,290 C150,360 330,440 545,420 L545,810 L0,810 Z" fill="var(--navy)"/>
  </svg>

  <div class="logo-spot"></div>
  <h1 class="practice-name">Kieferorthopädie Brunnweid</h1>
  <p class="doctor-name">Dr. med. dent. Lukas Venberg</p>
  <p class="doctor-title">Fachzahnarzt für Kieferorthopädie (CH)</p>

  <ul class="contact-list">
    <li class="contact-item">
      <span class="contact-icon"><svg viewBox="0 0 20 20"><path d="M2,10 L10,3 L18,10 M5,8 V17 H15 V8" fill="none" stroke="var(--navy)" stroke-width="2"/><rect x="8.5" y="12" width="3" height="5" fill="var(--navy)"/></svg></span>
      Talackerweg 7 - 8946 Schlieren
    </li>
    <li class="contact-item" style="width:375px">
      <span class="contact-icon"><svg viewBox="0 0 20 20"><rect x="6" y="2" width="8" height="16" rx="1.5" fill="var(--navy)"/><rect x="7.5" y="4.5" width="5" height="6" fill="var(--sky)"/></svg></span>
      044 618 42 50
    </li>
    <li class="contact-item">
      <span class="contact-icon"><svg viewBox="0 0 20 20"><circle cx="10" cy="10" r="7.5" fill="none" stroke="var(--navy)" stroke-width="1.8"/><ellipse cx="10" cy="10" rx="3.2" ry="7.5" fill="none" stroke="var(--navy)" stroke-width="1.5"/><path d="M2.5,10 H17.5" stroke="var(--navy)" stroke-width="1.5"/></svg></span>
      www.brunnweidpraxis.net
    </li>
    <li class="contact-item">
      <span class="contact-icon"><svg viewBox="0 0 20 20"><rect x="2.5" y="5" width="15" height="10.5" fill="none" stroke="var(--navy)" stroke-width="1.8"/><path d="M2.5,5 L10,11 L17.5,5" fill="none" stroke="var(--navy)" stroke-width="1.8"/></svg></span>
      info@brunnweidpraxis.net
    </li>
  </ul>
</section>

</body>
</html>
```